Building quality affordable homes in Brisbane, Australia for investors and families

We design, build and market our own homes from small single story to large 3 story luxury homes. Our main focus is "duel key" - that is two houses on one lot - a "zooky" (as in where The Zook lived) or attached granny flat.
We have a logo design and need a business card to suit. Something simple but eye catching. We want to communicate: "you are making a smart financial choice buying or building with us".
Unfortunately a lot of information has to be on the card including - Name, position, phone, mobile, fax, email, web address and of course the logo.
Logo in multiple formats and high res now available.

Target Market(s)

Families, contractors, real estate agents, other builders, developers, banks and home buyers.

Industry/Entity Type

Financial

Contact Information for Business Card

Name, position, phone, mobile, fax, email, web address

Font styles to use
Serif

Requirements
Must have
• The logo, and the details.
Nice to have
• Show or explain what we do - design, build and market affordable homes.
Should not have
• Nothing too fancy, outrageous - building companies are normally very straight.

```html
<!DOCTYPE html>
<html lang="en">
<head>
<meta charset="utf-8">
<title>Keystone Dwellings – Business Card</title>
<link href="https://fonts.googleapis.com/css2?family=Arimo:wght@400;700&family=Questrial&display=swap" rel="stylesheet">
<style>
  :root {
    --page-bg: #eceef1;
    --brand-blue: #1a6fc0;
    --brand-light: #7fa6d8;
    --deep-blue: #0b4fae;
    --mid-blue: #1f7fe0;
    --sky-blue: #4fb6f2;
    --card-white: #ffffff;
    --ink: #1d1d1d;
    --faint: #eeeeee;
  }
  * { margin: 0; padding: 0; box-sizing: border-box; }
  html, body { width: 1200px; height: 784px; overflow: hidden; }
  body { background: var(--page-bg); position: relative; font-family: "Arimo", Arial, sans-serif; }

  .card {
    position: absolute;
    width: 540px;
    height: 330px;
    overflow: hidden;
    box-shadow: 0 6px 18px rgba(0,0,0,0.18);
  }

  /* Back face */
  .card-back { left: 40px; top: 90px; background: var(--deep-blue); }
  .card-back .swoosh { position: absolute; inset: 0; width: 100%; height: 100%; }
  .tagline {
    position: absolute;
    left: 0; right: 0; top: 92px;
    text-align: center;
    font-family: "Questrial", "Century Gothic", sans-serif;
    color: var(--card-white);
    font-size: 15.5px;
    letter-spacing: 2.4px;
    line-height: 24px;
    text-transform: uppercase;
  }

  /* Front face */
  .card-front { left: 620px; top: 364px; background: var(--card-white); }
  .brand {
    position: absolute; left: 40px; top: 36px;
    display: flex; align-items: center; gap: 10px;
  }
  .brand-square { width: 72px; height: 72px; background: var(--brand-light); }
  .brand-name {
    color: var(--brand-blue);
    font-weight: 700;
    line-height: 1;
  }
  .brand-name .word { display: block; font-size: 34px; }
  .brand-name .sub { display: block; font-size: 12.5px; letter-spacing: 0.4px; margin-top: 4px; }
  .corner-mark {
    position: absolute; right: 40px; top: 90px;
    width: 110px; height: 110px; background: var(--faint);
  }

  .person { position: absolute; left: 40px; top: 150px; }
  .person-name { color: var(--brand-blue); font-size: 21px; font-weight: 400; }
  .person-role { color: var(--ink); font-size: 11px; margin-top: 3px; }

  .contacts { position: absolute; left: 40px; top: 212px; list-style: none; }
  .contacts li {
    display: flex; align-items: center; gap: 6px;
    font-size: 14px; color: var(--ink); line-height: 19px;
  }
  .contacts svg { width: 13px; height: 13px; flex: none; }
</style>
</head>
<body>

<section class="card card-back" aria-label="Business card back">
  <svg class="swoosh" viewBox="0 0 540 330" preserveAspectRatio="none" aria-hidden="true">
    <defs>
      <linearGradient id="back-fill" x1="0" y1="0" x2="1" y2="1">
        <stop offset="0" stop-color="#0d56b8"/>
        <stop offset="0.6" stop-color="#1a73d6"/>
        <stop offset="1" stop-color="#2a8ee6"/>
      </linearGradient>
      <linearGradient id="wave-fill" x1="0" y1="0" x2="1" y2="0">
        <stop offset="0" stop-color="#3aa4ee" stop-opacity="0.2"/>
        <stop offset="1" stop-color="#5cc3f5" stop-opacity="0.85"/>
      </linearGradient>
    </defs>
    <rect width="540" height="330" fill="url(#back-fill)"/>
    <path d="M120 330 C260 250 420 150 540 110 L540 330 Z" fill="url(#wave-fill)"/>
    <path d="M260 330 C360 260 460 200 540 175 L540 330 Z" fill="#1b7ad8" opacity="0.55"/>
    <path d="M0 240 C160 210 330 150 540 40" fill="none" stroke="#7fd0fa" stroke-width="1.2" opacity="0.7"/>
    <path d="M300 0 C330 120 300 240 210 330" fill="none" stroke="#6fc2f6" stroke-width="1" opacity="0.5"/>
    <circle cx="90" cy="170" r="160" fill="#0a4aa6" opacity="0.35"/>
  </svg>
  <p class="tagline">You are making a smart financial choice<br>buying or building with us</p>
</section>

<section class="card card-front" aria-label="Business card front">
  <div class="brand">
    <span class="brand-square" aria-hidden="true"></span>
    <span class="brand-name">
      <span class="word">Keystone</span>
      <span class="sub">DWELLINGS COMPANY PTY LTD</span>
    </span>
  </div>
  <span class="corner-mark" aria-hidden="true"></span>

  <div class="person">
    <p class="person-name">Dalton Reyes</p>
    <p class="person-role">Director</p>
  </div>

  <ul class="contacts">
    <li>
      <svg viewBox="0 0 13 13" aria-hidden="true"><rect x="3.5" y="0.5" width="6" height="12" rx="1" fill="#1a6fc0"/><rect x="4.5" y="2" width="4" height="7" fill="#fff"/></svg>
      0400 512 873
    </li>
    <li>
      <svg viewBox="0 0 13 13" aria-hidden="true"><path d="M2 1 L4.5 1 L5.5 4 L4 5 C5 7.5 6 8.5 8 9 L9 7.5 L12 8.5 L12 11 C7 12 1 6 2 1 Z" fill="#1a6fc0"/></svg>
      07 3210 4480
    </li>
    <li>
      <svg viewBox="0 0 13 13" aria-hidden="true"><rect x="1" y="5" width="11" height="7" rx="1" fill="#1a6fc0"/><rect x="3" y="1" width="7" height="5" fill="#fff" stroke="#1a6fc0"/></svg>
      07 3210 4481
    </li>
    <li>
      <svg viewBox="0 0 13 13" aria-hidden="true"><rect x="0.5" y="2.5" width="12" height="8" rx="1" fill="#1a6fc0"/><path d="M1 3 L6.5 7.5 L12 3" fill="none" stroke="#fff" stroke-width="1"/></svg>
      dalton@keystonedwellings.com.au
    </li>
    <li>
      <svg viewBox="0 0 13 13" aria-hidden="true"><circle cx="6.5" cy="6.5" r="6" fill="#1a6fc0"/><path d="M0.5 6.5 H12.5 M6.5 0.5 C3.5 4 3.5 9 6.5 12.5 M6.5 0.5 C9.5 4 9.5 9 6.5 12.5" fill="none" stroke="#fff" stroke-width="0.8"/></svg>
      www.keystonedwellings.com.au
    </li>
  </ul>
</section>

</body>
</html>
```